Upsell Vertical Banner Ad Design For B2B Marketing Agency Vertical 768px × 1180px IS THE SIZE

I need a banner made for my website www.brightlanepromotionhub.biz This banner will be an upsell advertisement for after someone signs up for my monthly program. When they login to their account for the 1st time I will give them the chance to upgrade their account to our annual program with just one click.

this is a page that upsells it currently to give you an idea how we market ourselves:
https://tlpx.pagevault-example.com/page/tlp-annual-upsell

Use this content:

Are You Ready To Commit To Taking Your Business To The Next Level?

Because We're In This For The Long-Haul and Dedicated To Your Success...

Save $300 By Upgrading To An Annual Membership And Pay Only $74/mth

((BUTTON))Yes, Upgrade My Plan Right Now!

*Must prepay the full year at only $898/yr!

Target Market(s)

business owners

Industry/Entity Type

Marketing

Requirements
Must have
• 768px × 1180px IS THE SIZE vertical

Use this content:

Nice to have
• Use this content:

Should not have
• Use this content:

```html
<!DOCTYPE html>
<html lang="en">
<head>
<meta charset="utf-8">
<title>Annual Membership Upgrade Banner</title>
<link href="https://fonts.googleapis.com/css2?family=Catamaran:wght@700;800;900&family=Source+Sans+3:wght@400;600;700&display=swap" rel="stylesheet">
<style>
  :root {
    --deep-blue: #3a8ad3;
    --mid-blue: #4fb6e4;
    --cyan: #7eeef9;
    --bright-cyan: #2fcbe6;
    --pale-blue: #b9e3f2;
    --white: #ffffff;
    --ink: #0c0c0c;
    --accent-blue: #2aa2df;
  }
  * { margin: 0; padding: 0; box-sizing: border-box; }
  html, body { width: 783px; height: 1200px; overflow: hidden; background: var(--white); }
  .banner {
    position: relative;
    width: 783px;
    height: 1200px;
    overflow: hidden;
    background: linear-gradient(35deg, var(--deep-blue) 0%, var(--mid-blue) 45%, var(--cyan) 100%);
    font-family: "Source Sans 3", "Helvetica Neue", Arial, sans-serif;
    color: var(--ink);
  }
  .backdrop { position: absolute; inset: 0; width: 783px; height: 1200px; }
  .line { position: absolute; white-space: nowrap; line-height: 1; }
  .headline { font-family: "Catamaran", "Arial Black", sans-serif; left: 42px; }
  .headline--ready { font-size: 94px; font-weight: 900; letter-spacing: 0.5px; }
  .headline--sub { font-size: 51px; font-weight: 800; }
  .headline--business { font-size: 70px; font-weight: 800; color: var(--white); }
  .tagline { left: 43px; font-size: 19px; font-weight: 400; }
  .offer { right: 46px; text-align: right; font-size: 31px; font-weight: 400; }
  .offer--save { font-size: 45px; font-weight: 700; }
  .offer--amount { font-size: 68px; font-weight: 700; color: var(--accent-blue); }
  .offer--plan { font-weight: 600; color: var(--accent-blue); }
  .offer--price { font-weight: 700; }
  .cta {
    left: 0; width: 760px; text-align: center;
    font-size: 22px; font-weight: 400;
  }
  .terms {
    left: 0; width: 760px; text-align: center;
    font-size: 29px; font-weight: 700; letter-spacing: 0.3px;
  }
</style>
</head>
<body>
  <main class="banner">
    <svg class="backdrop" viewBox="0 0 783 1200" aria-hidden="true">
      <defs>
        <linearGradient id="pale-fade" x1="0" y1="0" x2="1" y2="1">
          <stop offset="0" stop-color="#8fd2ec"/>
          <stop offset="1" stop-color="#d6f1f8"/>
        </linearGradient>
        <linearGradient id="corner-cyan" x1="0" y1="1" x2="1" y2="0">
          <stop offset="0" stop-color="#36c6e8"/>
          <stop offset="1" stop-color="#8cf2fb"/>
        </linearGradient>
      </defs>
      <polygon points="783,285 783,975 575,1200 0,1200" fill="var(--white)"/>
      <polygon points="0,560 395,905 575,1200 0,1200" fill="url(#pale-fade)" opacity="0.85"/>
      <polygon points="783,975 783,1200 575,1200" fill="url(#corner-cyan)"/>
      <polygon points="783,1060 783,1200 680,1200" fill="var(--bright-cyan)" opacity="0.6"/>
    </svg>

    <h1>
      <span class="line headline headline--ready" style="top:44px">ARE</span>
      <span class="line headline headline--ready" style="top:130px">YOU</span>
      <span class="line headline headline--ready" style="top:216px">READY</span>
      <span class="line headline headline--sub" style="top:318px">To Commit To Taking</span>
      <span class="line headline headline--business" style="top:380px">Your Business</span>
      <span class="line headline headline--sub" style="top:464px">To The Next Level?</span>
    </h1>

    <p class="line tagline" style="top:552px">Because We're In This For The Long-Haul</p>
    <p class="line tagline" style="top:580px">and Dedicated To Your Success...</p>

    <div class="offer-block">
      <p class="line offer offer--save" style="top:565px">Save</p>
      <p class="line offer offer--amount" style="top:605px">$300</p>
      <p class="line offer" style="top:678px">By Upgrading</p>
      <p class="line offer" style="top:721px">To An</p>
      <p class="line offer offer--plan" style="top:765px">Annual Membership</p>
      <p class="line offer" style="top:807px">And</p>
      <p class="line offer" style="top:851px">Pay Only</p>
      <p class="line offer offer--price" style="top:895px">$74/mth</p>
    </div>

    <p class="line cta" style="top:980px">Yes, Upgrade My Plan Right Now!</p>
    <p class="line terms" style="top:1040px">MUST PREPAY THE FULL YEAR</p>
    <p class="line terms" style="top:1080px">AT ONLY $898/YR!</p>
  </main>
</body>
</html>
```